Pulsar Vale Records

Projeto para pagina do facebook. Quero um design limpo e moderno, sem muita imagens pesadas. A é de uma gravadora de música eletrônica, voltada pro estilo Tech House, Techno, Deep House e Minimal.

Download Logomarca:

http://www14.arquivonuvem.com/v/83417205/file.html

Informações para colocar na capa.

Telefone:(11)4917-2586
Site: http://www.pulsarvale.fm
e-mail: contato@pulsarvale.fm
Ondalink: http://ondalink.net/pulsarvalerecords

```html
<!DOCTYPE html>
<html lang="pt-BR">
<head>
<meta charset="utf-8">
<title>Pulsar Vale Records – Capas</title>
<link rel="stylesheet" href="https://fonts.googleapis.com/css2?family=Open+Sans:wght@400;700&display=swap">
<style>
  :root {
    --stage-center: #ffffff;
    --stage-edge: #e6e6e4;
    --cover-dark: #111212;
    --cover-mid: #262727;
    --warm-dark: #1c1312;
    --warm-mid: #4a2a18;
    --warm-glow: #8a4a1c;
    --accent: #f28a1e;
    --text: #ffffff;
    --dash: rgba(255,255,255,0.35);
  }
  * { margin: 0; padding: 0; box-sizing: border-box; }
  html, body { width: 1200px; height: 1000px; overflow: hidden; }
  body {
    position: relative;
    background: radial-gradient(ellipse 62% 60% at 50% 50%, var(--stage-center) 55%, var(--stage-edge) 100%);
    font-family: "Open Sans", Tahoma, sans-serif;
    color: var(--text);
  }
  .cover {
    position: absolute;
    left: 174px;
    width: 851px;
    height: 315px;
    overflow: hidden;
  }
  .cover--plain {
    top: 133px;
    background:
      radial-gradient(ellipse 70% 80% at 60% 95%, var(--cover-mid) 0%, transparent 70%),
      linear-gradient(180deg, var(--cover-dark) 0%, #1a1b1b 100%);
  }
  .cover--warm { top: 552px; }
  .cover__backdrop {
    position: absolute; inset: 0;
    background:
      radial-gradient(ellipse 30% 45% at 35% 35%, rgba(160,90,40,0.55) 0%, transparent 70%),
      radial-gradient(ellipse 18% 55% at 89% 55%, rgba(170,80,40,0.55) 0%, transparent 75%),
      radial-gradient(ellipse 60% 60% at 50% 90%, var(--warm-glow) 0%, transparent 70%),
      linear-gradient(180deg, var(--warm-dark) 0%, var(--warm-mid) 100%);
  }
  .brand {
    position: absolute;
    left: 238px;
    top: 145px;
    display: flex;
    align-items: center;
    gap: 10px;
  }
  .brand__dot {
    width: 26px; height: 26px;
    border-radius: 50%;
    background: var(--accent);
  }
  .brand__name {
    font-weight: 700;
    font-size: 34px;
    line-height: 1;
    letter-spacing: -0.5px;
    color: var(--text);
    white-space: nowrap;
  }
  .contact {
    position: absolute;
    left: 246px;
    top: 235px;
    list-style: none;
    font-size: 12.5px;
    line-height: 17px;
    white-space: nowrap;
  }
  .about {
    position: absolute;
    left: 625px;
    top: 222px;
    width: 240px;
    height: 110px;
    border: 1px dashed var(--dash);
    border-radius: 8px 0 0 0;
    padding: 12px 0 0 19px;
    font-size: 12.5px;
    line-height: 17px;
    white-space: nowrap;
  }
</style>
</head>
<body>
  <section class="cover cover--plain" aria-label="Capa escura">
    <div class="brand">
      <span class="brand__dot"></span>
      <span class="brand__name">Pulsar Vale Records</span>
    </div>
    <ul class="contact">
      <li>Site: http://pulsarvale.fm</li>
      <li>e-mail: contato@pulsarvale.fm</li>
      <li>Ondalink: http://ondalink.net/pulsarvalerecords</li>
      <li>Tel.: (11) 4917-2586</li>
    </ul>
    <p class="about">A Pulsar Vale Records é uma<br>gravadora de música eletrônica,<br>voltada pro estilo Tech House,<br>Techno, Deep House e Minimal.</p>
  </section>

  <section class="cover cover--warm" aria-label="Capa com fundo luminoso">
    <div class="cover__backdrop" role="img" aria-label="Fundo de luzes desfocadas em tons de laranja e marrom, formando colunas como um equalizador"></div>
    <div class="brand">
      <span class="brand__dot"></span>
      <span class="brand__name">Pulsar Vale Records</span>
    </div>
    <ul class="contact">
      <li>Site: http://pulsarvale.fm</li>
      <li>e-mail: contato@pulsarvale.fm</li>
      <li>Ondalink: http://ondalink.net/pulsarvalerecords</li>
      <li>Tel.: (11) 4917-2586</li>
    </ul>
    <p class="about">A Pulsar Vale Records é uma<br>gravadora de música eletrônica,<br>voltada pro estilo Tech House,<br>Techno, Deep House e Minimal.</p>
  </section>
</body>
</html>
```